Business card for auto dealership

Looking for a clean modern design.
Would like attached logo incorporated

Industry/Entity Type

Car dealership

Contact Information for Business Card

Name, website, phone, cell, fax, email

```html
<!DOCTYPE html>
<html lang="en">
<head>
<meta charset="utf-8">
<title>Halden Truck &amp; Auto Sales – Business Card</title>
<link rel="stylesheet" href="https://fonts.googleapis.com/css2?family=Kaushan+Script&family=Open+Sans:wght@400;700&display=swap">
<style>
  :root {
    --backdrop: #3a3a3c;
    --card-black: #1c1c1e;
    --card-white: #ffffff;
    --ink: #1a1a1a;
    --silver-light: #e6e6e6;
    --silver-mid: #a9a9a9;
    --silver-dark: #6f6f6f;
    --logo-front: #c9c9c9;
    --logo-back: #ffffff;
  }
  * { margin: 0; padding: 0; box-sizing: border-box; }
  html, body {
    width: 1200px; height: 962px; overflow: hidden;
    background: var(--backdrop);
  }
  .stage {
    position: relative; width: 1200px; height: 962px;
    display: flex; flex-direction: column; align-items: center; justify-content: center; gap: 56px;
  }
  .card {
    position: relative; width: 620px; height: 354px;
    border-radius: 22px; overflow: hidden;
    box-shadow: 0 14px 30px rgba(0,0,0,.45);
  }
  .card-front { background: var(--card-black); display: flex; align-items: center; justify-content: center; }
  .card-back { background: var(--card-black); }

  .wordmark {
    font-family: 'Open Sans', sans-serif; font-weight: 700;
    text-align: center; line-height: 1;
  }
  .wordmark-name { display: block; letter-spacing: -1px; }
  .wordmark-tag { display: block; letter-spacing: 1px; text-transform: uppercase; }
  .card-front .wordmark { color: var(--logo-front); }
  .card-front .wordmark-name { font-size: 118px; }
  .card-front .wordmark-tag { font-size: 24px; margin-top: 6px; }

  .back-panel {
    position: absolute; inset: 0; width: 100%; height: 100%;
  }
  .contact-block {
    position: absolute; left: 38px; top: 44px; width: 270px;
  }
  .holder-name {
    font-family: 'Kaushan Script', cursive; font-size: 34px; color: var(--ink);
    margin-bottom: 18px; padding-left: 14px;
  }
  .contact-list { list-style: none; }
  .contact-item {
    display: flex; align-items: center; gap: 10px;
    font-family: 'Open Sans', sans-serif; font-size: 17px; color: var(--ink);
    line-height: 1.45;
  }
  .contact-item.is-text { font-size: 15px; }
  .contact-icon { width: 14px; height: 14px; flex: none; fill: var(--ink); }

  .card-back .wordmark {
    position: absolute; left: 370px; top: 196px; width: 230px; color: var(--logo-back);
  }
  .card-back .wordmark-name { font-size: 56px; }
  .card-back .wordmark-tag { font-size: 12px; margin-top: 4px; }
</style>
</head>
<body>
<main class="stage">
  <section class="card card-front" aria-label="Card front">
    <div class="wordmark">
      <span class="wordmark-name">Halden</span>
      <span class="wordmark-tag">Truck &amp; Auto Sales</span>
    </div>
  </section>

  <section class="card card-back" aria-label="Card back">
    <svg class="back-panel" viewBox="0 0 620 354" preserveAspectRatio="none" aria-hidden="true">
      <defs>
        <linearGradient id="silver" x1="0" y1="0" x2="1" y2="0">
          <stop offset="0" stop-color="var(--silver-dark)"/>
          <stop offset=".5" stop-color="var(--silver-light)"/>
          <stop offset="1" stop-color="var(--silver-mid)"/>
        </linearGradient>
      </defs>
      <polygon points="0,0 330,0 300,354 0,354" fill="var(--card-white)"/>
      <polygon points="318,0 330,0 300,354 276,354" fill="url(#silver)"/>
      <polygon points="334,0 342,0 322,354 306,354" fill="url(#silver)"/>
      <polygon points="346,0 352,0 338,354 326,354" fill="url(#silver)" opacity=".8"/>
    </svg>

    <div class="contact-block">
      <p class="holder-name">Dana Whitfield</p>
      <ul class="contact-list">
        <li class="contact-item">
          <svg class="contact-icon" viewBox="0 0 24 24" aria-label="Phone"><path d="M6.6 10.8a15 15 0 0 0 6.6 6.6l2.2-2.2a1 1 0 0 1 1-.25 11.4 11.4 0 0 0 3.6.57 1 1 0 0 1 1 1V20a1 1 0 0 1-1 1A17 17 0 0 1 3 4a1 1 0 0 1 1-1h3.5a1 1 0 0 1 1 1c0 1.25.2 2.45.57 3.57a1 1 0 0 1-.25 1z"/></svg>
          555-210-4836
        </li>
        <li class="contact-item">
          <svg class="contact-icon" viewBox="0 0 24 24" aria-label="Mobile"><path d="M7 1h10a2 2 0 0 1 2 2v18a2 2 0 0 1-2 2H7a2 2 0 0 1-2-2V3a2 2 0 0 1 2-2zm0 3v14h10V4zm5 15.5a1 1 0 1 0 0 2 1 1 0 0 0 0-2z"/></svg>
          555-347-9152
        </li>
        <li class="contact-item">
          <svg class="contact-icon" viewBox="0 0 24 24" aria-label="Fax"><path d="M7 2h10v5H7zM4 8h16a2 2 0 0 1 2 2v7h-4v5H6v-5H2v-7a2 2 0 0 1 2-2zm4 8v4h8v-4z"/></svg>
          555-682-0417
        </li>
        <li class="contact-item is-text">
          <svg class="contact-icon" viewBox="0 0 24 24" aria-label="Email"><path d="M2 5h20v14H2zm2 2v.5l8 5 8-5V7l-8 5z"/></svg>
          dana@haldenauto.com
        </li>
        <li class="contact-item is-text">
          <svg class="contact-icon" viewBox="0 0 24 24" aria-label="Website"><path d="M12 2a10 10 0 1 0 0 20 10 10 0 0 0 0-20zm0 2c.9 0 2.3 2.2 2.8 7H9.2c.5-4.8 1.9-7 2.8-7zM4.1 11a8 8 0 0 1 3.3-5.6A15 15 0 0 0 7.2 11zm0 2h3.1a15 15 0 0 0 .2 5.6A8 8 0 0 1 4.1 13zm5.1 0h5.6c-.5 4.8-1.9 7-2.8 7s-2.3-2.2-2.8-7zm7.6 0h3.1a8 8 0 0 1-3.3 5.6 15 15 0 0 0 .2-5.6zm0-2a15 15 0 0 0-.2-5.6 8 8 0 0 1 3.3 5.6z"/></svg>
          Haldenauto.com
        </li>
      </ul>
    </div>

    <div class="wordmark">
      <span class="wordmark-name">Halden</span>
      <span class="wordmark-tag">Truck &amp; Auto Sales</span>
    </div>
  </section>
</main>
</body>
</html>
```